Healer at the Hearth needs business card

We need a business card that reflects the look and feel of the new website at www.healerathearth.ca

Target Market(s)

Our patient navigation and advocacy services are most commonly used by seniors who feel overwhelmed by the health care system and want someone on their side to advocate for their care. Individuals with ill parents or other family members may also come to rely on Healer at the Hearth to help them support their loved one through their health care journey. Ultimately, anyone who finds their health care experience challenging and wants someone completely focused on their needs can benefit from the services of our doctor / nurse team.

Industry/Entity Type

Business

Requirements
Must have
• One design tailored for two clinician which should include: logo, name, title, tel, email, web address and tagline
Nice to have
• A banner image to create a similar look to the website at www.healerathearth.ca
Should not have
• Too cluttered or busy - must be clean and professional

```html
<!DOCTYPE html>
<html lang="en">
<head>
<meta charset="utf-8">
<title>Healer at the Hearth – Business Cards</title>
<link rel="stylesheet" href="https://fonts.googleapis.com/css2?family=Open+Sans:wght@400;700&family=Nothing+You+Could+Do&display=swap">
<style>
  :root {
    --page: #ffffff;
    --card: #ffffff;
    --brand-blue: #2e5f86;
    --brand-red: #a31c33;
    --ink-grey: #6a6a6a;
    --ink-soft: #6f6f6f;
    --nurse-accent: #a31c33;
    --doctor-accent: #2e6a92;
    --nurse-banner-start: #f4f4f4;
    --nurse-banner-end: #efe3e3;
    --doctor-banner-start: #dfeaf5;
    --doctor-banner-end: #eadfd6;
    --shadow: rgba(0, 0, 0, 0.32);
  }
  * { box-sizing: border-box; margin: 0; padding: 0; }
  html, body {
    width: 1043px;
    height: 1200px;
    overflow: hidden;
    background: var(--page);
  }
  body { position: relative; font-family: "Open Sans", sans-serif; }

  .card {
    position: absolute;
    left: 52px;
    width: 935px;
    height: 520px;
    background: var(--card);
    border-radius: 28px;
    box-shadow: 0 4px 14px var(--shadow);
    overflow: hidden;
  }
  .card--nurse { top: 49px; --accent: var(--nurse-accent); }
  .card--doctor { top: 625px; --accent: var(--doctor-accent); }

  .brand__mark {
    position: absolute;
    left: 52px;
    top: 54px;
    width: 92px;
    height: 92px;
    border-radius: 50%;
    background: var(--brand-red);
  }
  .brand__name {
    position: absolute;
    left: 163px;
    top: 80px;
    color: var(--brand-blue);
    font-size: 36px;
    line-height: 41px;
    font-weight: 400;
    letter-spacing: -0.5px;
  }

  .person {
    position: absolute;
    left: 495px;
    top: 78px;
  }
  .person__name {
    color: var(--ink-grey);
    font-size: 34px;
    line-height: 44px;
    font-weight: 400;
    white-space: nowrap;
  }
  .person__name strong { font-weight: 700; }
  .person__role {
    color: var(--ink-soft);
    font-size: 26px;
    line-height: 34px;
    margin-top: 2px;
  }

  .banner {
    position: absolute;
    left: 0;
    top: 188px;
    width: 100%;
    height: 195px;
  }
  .banner__photo { position: absolute; inset: 0; }
  .card--nurse .banner__photo {
    background: linear-gradient(90deg, var(--nurse-banner-start), var(--nurse-banner-end));
  }
  .card--doctor .banner__photo {
    background: linear-gradient(90deg, var(--doctor-banner-start), var(--doctor-banner-end));
  }
  .banner__tagline {
    position: absolute;
    left: 62px;
    top: 33px;
    font-family: "Nothing You Could Do", cursive;
    font-size: 29px;
    line-height: 45px;
    color: var(--accent);
  }

  .contact__web {
    position: absolute;
    left: 52px;
    top: 446px;
    font-size: 27px;
    line-height: 36px;
    color: var(--accent);
  }
  .contact__line {
    position: absolute;
    left: 488px;
    display: flex;
    align-items: center;
    gap: 10px;
    font-size: 27px;
    line-height: 36px;
    color: var(--ink-soft);
  }
  .contact__line--phone { top: 400px; }
  .contact__line--email { top: 446px; }
  .contact__icon { width: 28px; height: 28px; flex: none; }
  .contact__icon rect, .contact__icon .fill { fill: var(--accent); }
</style>
</head>
<body>

  <section class="card card--nurse">
    <span class="brand__mark"></span>
    <p class="brand__name">Healer at<br>the Hearth</p>
    <div class="person">
      <h1 class="person__name"><strong>Maren Holloway</strong>, RN</h1>
      <p class="person__role">Co-Founder</p>
    </div>
    <div class="banner">
      <div class="banner__photo" role="img" aria-label="Banner photo: a hand holding a red heart beside a stethoscope"></div>
      <p class="banner__tagline">Treating you<br>like a member<br>of our family</p>
    </div>
    <p class="contact__web">www.healerathearth.ca</p>
    <p class="contact__line contact__line--phone">
      <svg class="contact__icon" viewBox="0 0 28 28" aria-hidden="true">
        <rect width="28" height="28" rx="3"/>
        <path d="M9 6c1 0 2 2.5 2.5 3.5.3.8-.8 1.6-1.2 2.2.9 2.2 2.6 4 4.8 5 .6-.5 1.4-1.6 2.2-1.3 1 .5 3.5 1.6 3.5 2.6 0 1.4-1.6 3-3 3C11.5 21 7 16.5 7 10c0-1.6 1-4 2-4z" fill="#fff"/>
      </svg>
      647-555-0143
    </p>
    <p class="contact__line contact__line--email">
      <svg class="contact__icon" viewBox="0 0 28 28" aria-hidden="true">
        <path class="fill" d="M2 6h24v16H2z"/>
        <path d="M2 6l12 9 12-9" fill="none" stroke="#fff" stroke-width="1.6"/>
      </svg>
      info@healerathearth.ca
    </p>
  </section>

  <section class="card card--doctor">
    <span class="brand__mark"></span>
    <p class="brand__name">Healer at<br>the Hearth</p>
    <div class="person">
      <h1 class="person__name"><strong>Julian Ferrante</strong>, MD</h1>
      <p class="person__role">Co-Founder</p>
    </div>
    <div class="banner">
      <div class="banner__photo" role="img" aria-label="Banner photo: caring hands clasped together on a soft blue background"></div>
      <p class="banner__tagline">Treating you<br>like a member<br>of our family</p>
    </div>
    <p class="contact__web">www.healerathearth.ca</p>
    <p class="contact__line contact__line--phone">
      <svg class="contact__icon" viewBox="0 0 28 28" aria-hidden="true">
        <rect width="28" height="28" rx="3"/>
        <path d="M9 6c1 0 2 2.5 2.5 3.5.3.8-.8 1.6-1.2 2.2.9 2.2 2.6 4 4.8 5 .6-.5 1.4-1.6 2.2-1.3 1 .5 3.5 1.6 3.5 2.6 0 1.4-1.6 3-3 3C11.5 21 7 16.5 7 10c0-1.6 1-4 2-4z" fill="#fff"/>
      </svg>
      647-555-0143
    </p>
    <p class="contact__line contact__line--email">
      <svg class="contact__icon" viewBox="0 0 28 28" aria-hidden="true">
        <path class="fill" d="M2 6h24v16H2z"/>
        <path d="M2 6l12 9 12-9" fill="none" stroke="#fff" stroke-width="1.6"/>
      </svg>
      info@healerathearth.ca
    </p>
  </section>

</body>
</html>
```